Billboard design for dentist that sees only children

I own a 12' x 25' digital billboard and I need help with billboard design. My wife is a general dentist that only sees children and is very passionate about giving them a quality dental experience . She has a great reputation in town. Obviously with a billboard there can't be a lot of reading. Maybe something that shows safety, love, experience and children. I am completely open to your ideas. In addition I have other businesses that also need billboard design so this could lead to more work. If you go to Maplecovedental.com under the about section you will find more information about the practice and our phone number. Attached is our logo which could be changed and content specs for the digital billboard. Happy Designing!!

Target Market(s)

Parents with children

Colors

Designer to choose colors to be used in the design.

Requirements
Must have
• Must attract attention and be nice to look at.
Nice to have
• Probably should have children in the picture ..... Maybe
Should not have
• If I see something I don't like I will let you know

```html
<!DOCTYPE html>
<html lang="en">
<head>
<meta charset="utf-8">
<title>Maple Cove Dental – Billboard</title>
<link rel="stylesheet" href="https://fonts.googleapis.com/css2?family=Signika:wght@400&family=Arimo:wght@400&display=swap">
<style>
  :root {
    --navy: #1a1464;
    --deep-blue: #2a2f8a;
    --sky-blue: #0793d8;
    --mid-blue: #2b8fc9;
    --teal-green: #22876a;
    --white: #ffffff;
    --page: #eeeeea;
    --photo-warm: #d9b7a0;
    --photo-cool: #5a9c6a;
  }
  * { margin: 0; padding: 0; box-sizing: border-box; }
  html, body {
    width: 1200px; height: 888px; overflow: hidden;
    background: var(--page);
  }
  .billboard {
    position: absolute; left: 0; top: 157px;
    width: 1200px; height: 574px;
    background: var(--white);
    overflow: hidden;
  }
  .billboard__art { position: absolute; inset: 0; }
  .kids-photo {
    position: absolute; left: 16px; top: 123px;
    width: 463px; height: 451px;
    border-radius: 120px 140px 0 0;
    background:
      radial-gradient(ellipse at 60% 35%, #f0d2bd 0%, transparent 45%),
      linear-gradient(160deg, #8a5a3c 0%, var(--photo-warm) 35%, #7ec3dc 60%, var(--photo-cool) 85%, #3d6fa0 100%);
  }
  .brand {
    position: absolute; right: 32px; top: 340px;
    text-align: right;
  }
  .brand__name {
    font-family: "Signika", sans-serif; font-weight: 400;
    font-size: 76px; line-height: 1; letter-spacing: 0.5px;
    color: var(--teal-green);
  }
  .brand__tagline {
    font-family: "Signika", sans-serif; font-style: italic; font-weight: 400;
    font-size: 35px; line-height: 1.1; margin-top: 2px; margin-right: 6px;
    color: var(--navy);
  }
  .web-address {
    position: absolute; left: 600px; width: 490px; top: 518px;
    text-align: center;
    font-family: "Arimo", sans-serif; font-size: 40px; line-height: 56px;
    color: var(--white);
  }
</style>
</head>
<body>
  <main class="billboard">
    <svg class="billboard__art" width="1200" height="574" viewBox="0 0 1200 574" aria-hidden="true">
      <defs>
        <linearGradient id="sky-band" x1="0" y1="0" x2="1" y2="0">
          <stop offset="0" stop-color="var(--deep-blue)"/>
          <stop offset="0.25" stop-color="var(--sky-blue)"/>
          <stop offset="0.6" stop-color="var(--mid-blue)"/>
          <stop offset="1" stop-color="var(--navy)"/>
        </linearGradient>
        <linearGradient id="base-band" x1="0" y1="0" x2="1" y2="0">
          <stop offset="0" stop-color="var(--navy)"/>
          <stop offset="0.5" stop-color="var(--sky-blue)"/>
          <stop offset="1" stop-color="var(--navy)"/>
        </linearGradient>
      </defs>
      <rect class="sky-band" x="0" y="0" width="1200" height="200" fill="url(#sky-band)"/>
      <path class="wave-white" d="M0,112 C300,30 600,130 850,168 C1000,190 1100,140 1200,108 L1200,520 L0,520 Z" fill="var(--white)"/>
      <path class="wave-green" d="M0,101 C300,19 600,119 850,157 C1000,179 1100,129 1200,97" fill="none" stroke="var(--teal-green)" stroke-width="22"/>
      <circle class="emblem-disc" cx="850" cy="213" r="124" fill="var(--white)"/>
      <rect class="base-band" x="0" y="515" width="1200" height="59" fill="url(#base-band)"/>
    </svg>

    <div class="kids-photo" role="img" aria-label="Photo of four laughing children leaning together, a boy in a green plaid shirt in front"></div>

    <div class="brand">
      <h1 class="brand__name">Maple Cove Dental</h1>
      <p class="brand__tagline">general dentistry for children</p>
    </div>

    <p class="web-address">www.maplecovedental.com</p>
  </main>
</body>
</html>
```